Flyers

Modify Existing Flyer and create another for exterior company
Updates

Previous Brief has been updated- we want to update this existing one also

Target Market(s)

Exterior Remodeling Customers

Industry/Entity Type

Remodeling/Construction

```html
<!DOCTYPE html>
<html lang="en">
<head>
<meta charset="utf-8">
<title>NorthPeak Roofing and Exteriors – Remodeling Flyer</title>
<link href="https://fonts.googleapis.com/css2?family=Montserrat:wght@400;500;600;700;800&display=swap" rel="stylesheet">
<style>
:root{
  --ink:#111111;
  --orange:#f15a24;
  --blue:#1f73c0;
  --blue-deep:#1a66b3;
  --text:#1e1e1e;
  --paper:#f4f4f4;
  --stage:#e9e9e9;
  --white:#ffffff;
}
*{margin:0;padding:0;box-sizing:border-box}
html,body{width:699px;height:1200px;overflow:hidden;background:var(--stage);font-family:'Montserrat',sans-serif;color:var(--text)}
.flyer{position:absolute;left:19px;top:172px;width:660px;height:855px;background:linear-gradient(180deg,#fafafa,var(--paper));box-shadow:0 4px 14px rgba(0,0,0,.18);overflow:hidden}
.shape{position:absolute;left:0;top:0;width:660px;height:427px}
.brand-block{background:var(--ink);clip-path:polygon(0 0,301px 0,209px 135px,0 135px)}
.photo-kitchen{background:linear-gradient(160deg,#e6e4e0 0%,#c9c6c0 40%,#6e655d 80%,#4a433d 100%);clip-path:polygon(0 135px,205px 135px,436px 356px,346px 427px,0 427px)}
.photo-bath{background:linear-gradient(180deg,#5a3a26 0%,#c9beb6 30%,#9a5a33 60%,#6b3e22 100%);clip-path:polygon(301px 0,660px 0,660px 356px,439px 356px,209px 135px)}
.band-call{background:var(--blue);clip-path:polygon(439px 356px,660px 356px,660px 427px,346px 427px)}
.band-local{background:var(--orange);clip-path:polygon(0 390px,297px 390px,330px 427px,0 427px)}
.divider{position:absolute;left:0;top:0}
.brand-name{position:absolute;left:22px;top:46px;width:180px;text-align:center;color:var(--white);font-weight:700;font-size:15px;line-height:20px;letter-spacing:.5px}
.headline{position:absolute;left:22px;top:318px;font-weight:700;line-height:1;color:var(--white);text-shadow:-1px -1px 0 var(--ink),1px -1px 0 var(--ink),-1px 1px 0 var(--ink),1px 1px 0 var(--ink)}
.headline .lead{display:block;font-size:18px;font-weight:600;letter-spacing:-.3px}
.headline .key{display:block;font-size:23px;font-weight:800;margin-top:5px;letter-spacing:-.5px}
.headline .or{font-size:15px;color:var(--white)}
.c-orange{color:var(--orange)}
.c-blue{color:var(--blue)}
.local-note{position:absolute;left:22px;top:392px;color:var(--white);font-size:12px;line-height:17px;font-weight:500}
.local-note strong{font-weight:800}
.call-box{position:absolute;left:449px;top:361px;color:var(--white);font-size:13px;line-height:15px;font-weight:500}
.call-box .free{color:var(--orange);font-weight:700}
.call-box .phone{display:block;font-size:25px;font-weight:700;line-height:30px;margin-top:2px}
.service{position:absolute}
.service h2{font-size:15.5px;font-weight:700;line-height:18px;color:var(--blue)}
.service h2 span{color:var(--orange)}
.service p{font-size:10.6px;line-height:13px;margin-top:2px;text-align:justify}
.service ul{list-style:none;margin:9px 0 0 13px}
.service li{font-size:10.6px;line-height:15px}
.service li::before{content:"• "}
.icon{position:absolute;width:40px;height:36px;fill:none;stroke:var(--blue);stroke-width:1.6}
.svc-kitchen{left:73px;top:451px;width:248px}
.svc-additions{left:419px;top:451px;width:218px}
.svc-bath{left:73px;top:659px;width:248px}
.svc-decks{left:419px;top:659px;width:218px}
.ic-kitchen{left:22px;top:462px}
.ic-additions{left:366px;top:460px}
.ic-bath{left:22px;top:666px}
.ic-decks{left:368px;top:666px}
.rule{position:absolute;left:0;top:819px;width:660px;height:4px;background:var(--orange)}
.footer{position:absolute;left:0;top:826px;width:660px;height:29px;background:var(--blue-deep);color:var(--white);font-weight:700;font-size:14px;line-height:29px;text-align:center;letter-spacing:.5px}
</style>
</head>
<body>
<div class="flyer">
  <div class="shape photo-kitchen" role="img" aria-label="Bright modern kitchen with grey island, pendant lights and dining area"></div>
  <div class="shape photo-bath" role="img" aria-label="Remodeled bathroom with wood-slat walls, freestanding tub and vanity"></div>
  <div class="shape brand-block"></div>
  <div class="shape band-call"></div>
  <div class="shape band-local"></div>
  <svg class="divider" width="660" height="427" viewBox="0 0 660 427">
    <polyline points="205,135 439,356 346,427" fill="none" stroke="#ffffff" stroke-width="4"/>
  </svg>

  <div class="brand-name">NorthPeak<br>Roofing and Exteriors</div>

  <h1 class="headline">
    <span class="lead">Ready for a Beautiful and Functional</span>
    <span class="key"><span class="c-orange">KITUCHEN</span> <span class="or">or</span> <span class="c-blue">BATHROOM?</span></span>
  </h1>

  <p class="local-note">WORK WITH A <strong>TOP-RATED</strong> LOCAL<br>REMODELING COMPANY IN <strong>ANKENY,AI</strong></p>

  <p class="call-box">CALL TODAY FOR YOUR<br><span class="free">FREE</span> ESTIMATE<span class="phone">555-214-0187</span></p>

  <svg class="icon ic-kitchen" viewBox="0 0 40 36"><rect x="2" y="2" width="10" height="7"/><rect x="28" y="2" width="10" height="7"/><path d="M20 4v4M15 14h10l-2-5h-6z"/><rect x="2" y="20" width="36" height="14"/><path d="M2 25h36M14 25v9M26 25v9"/></svg>
  <section class="service svc-kitchen">
    <h2>KITICHEN <span>REMODELING</span></h2>
    <p>Whatever your vision is for your new kitchen our crew can help you bring it to life. You can trust us for:</p>
    <ul>
      <li>Open concept design services</li>
      <li>Kitchen cabinet installation services</li>
      <li>Kitchen counter top installation services</li>
      <li>Tile installation services</li>
      <li>Plumbing upgrade services</li>
      <li>Electrical upgrade services</li>
      <li>Drywall services</li>
      <li>Painting services</li>
    </ul>
  </section>

  <svg class="icon ic-additions" viewBox="0 0 40 36"><path d="M2 10L38 2v6"/><rect x="5" y="12" width="30" height="18"/><path d="M10 16h20v10H10zM15 16v10M20 16v10M25 16v10M1 32h38"/></svg>
  <section class="service svc-additions">
    <h2>HOME <span>ADDITIONS</span></h2>
    <p>No matter what kind of space you need, our team will bring your vision to life. You can hire us if you need a:</p>
    <ul>
      <li>Bathroom addition</li>
      <li>Bedreoom addition</li>
      <li>Garage addition</li>
      <li>Basement addition</li>
      <li>Guest room addition</li>
      <li>Living room addition</li>
      <li>Sunroom addition</li>
    </ul>
  </section>

  <svg class="icon ic-bath" viewBox="0 0 40 36"><path d="M12 10h16M16 10V5h8v5M20 3v2"/><rect x="8" y="12" width="24" height="20"/><path d="M20 12v20M8 18h24M10 32v3M30 32v3"/></svg>
  <section class="service svc-bath">
    <h2>BATHROOM <span>REMODELING</span></h2>
    <p>When you hire us for your bathroom remodeling project, the possibilities are endless. Our experienced and talented team can:</p>
    <ul>
      <li>Install a sutom tile shower</li>
      <li>Build a new vanity</li>
      <li>Install flooring and tile</li>
      <li>Replace your plumbing and light fixtures</li>
    </ul>
  </section>

  <svg class="icon ic-decks" viewBox="0 0 40 36"><path d="M10 12a12 9 0 0 1 24 0zM22 3v22M4 18l6 10h22M8 34l4-6M30 34l-2-6M3 28h34"/></svg>
  <section class="service svc-decks">
    <h2>DECKS/<span>PATIOS</span></h2>
    <p>An outdoor space is a great addition to any residential property. When you decide to build a patio or deck, you'll be able to experience a variety of benefits. Your outdoor area will increase your:</p>
    <ul>
      <li>Property value</li>
      <li>Curb appeal</li>
      <li>Functional living space</li>
    </ul>
  </section>

  <div class="rule"></div>
  <footer class="footer">www.northpeakhome.com</footer>
</div>
</body>
</html>
```